Create our new Brightcup Coffee Syrup Label designs. A delicious job!

Design a front label for a range of coffee syrup flavours. The brand is 'Brightcup Coffee Syrups'. The flavours, vanilla, hazelnut and caramel.
Our coffee syrups are made with only natural colours and flavours and are positioned in the popular premium space in Australian and international cafes.
The labels will be applied to 750 ml Boston Bottles (see attached image).
Given that coffee syrups are often positioned in high visibility locations in cafes, they can be considered as objects of functional beauty.
This range is a sub brand for our company and I have attached our main brand images in the flavours we want. we want this brand to look different to this Marlowe branded range, but included the image to show what we are currently doing in this space.
The different flavours can be identified by a combination of colour and text, which may be a line or section of the otherwise same overall design.
We are going to do a 2 part label with the front just carrying Brand and flavour descriptors plus 750 ml.
Total Bottle height is 240 mm bottle width is 70 mm

Target Market(s)

Cafe patrons, primarily women, 18-35, Middle class in terms of economics, regular cafe patrons. Who are looking for a guilt free treat in their busy day.

Logo Text

Brightcup Coffee Syrups Vanilla (or Hazelnut, or Caramel) 750 ml

Logo styles of interest
Pictorial/Combination Logo
Font styles to use
Sans Serif

Colors

Designer to choose colors to be used in the design.

Requirements
Must have
• A clear design, which is a combination of font and image. it needs to be legible from up to 2m away (across a counter in a cafe).
• We would like to see a device, which may be a gold drop, that may be the 'brightcup' meant to the coffee.
• The way our coffee syrups are used is by adding a small amount (15 ml) to a cup
• of coffee, this adds both flavour and sweetness to the overall coffee experience, and cafes charge a premium for this service. We want our package to show this will be a great thing to do.
• We have a few options in terms of Label stock. We can print on a foil, that will allow a metallic sheen to come through the colours (see example of the Marlowe branded bottles.
Nice to have
• We are looking for a modern, clean and distinctive look and feel to this range.
• I have added a key line for the front and back label, however we can create a different label die line should the design warrant that. Note this is just for the front label.
Should not have
• Difficult to read fonts or imagery that is not clear.
• Should look different to the Marlowe branded product range.

```html
<!DOCTYPE html>
<html lang="en">
<head>
<meta charset="utf-8">
<title>Brightcup Coffee Syrup Labels</title>
<link rel="stylesheet" href="https://fonts.googleapis.com/css2?family=Cabin+Condensed:wght@400;500&display=swap">
<style>
  :root {
    --page: #ffffff;
    --label-bg: #231f20;
    --label-edge: #2e2a2b;
    --brand-ink: #ffffff;
    --band-ink: #231f20;
    --copper-dark: #6b1d0e;
    --copper-mid: #b06a2c;
    --copper-light: #f2d3b2;
    --silver-dark: #8d8e92;
    --silver-mid: #c9cacd;
    --silver-light: #f4f4f5;
    --gold-dark: #c99a1a;
    --gold-mid: #f2cc47;
    --gold-light: #fff4b8;
  }
  html, body {
    margin: 0;
    padding: 0;
    width: 1200px;
    height: 1200px;
    overflow: hidden;
    background: var(--page);
  }
  .canvas {
    position: relative;
    width: 1200px;
    height: 1200px;
    font-family: "Cabin Condensed", "Arial Narrow", sans-serif;
  }
  .label {
    position: absolute;
    top: 352px;
    width: 304px;
    height: 474px;
    box-sizing: border-box;
    background: var(--label-bg);
    border: 3px solid var(--label-edge);
    overflow: hidden;
  }
  .label--hazelnut { left: 72px; }
  .label--vanilla { left: 427px; }
  .label--caramel { left: 805px; }

  .label__brand {
    position: absolute;
    top: 40px;
    left: 0;
    width: 100%;
    text-align: center;
    font-size: 44px;
    font-weight: 400;
    color: var(--brand-ink);
    line-height: 1;
    letter-spacing: 0.5px;
  }
  .label__emblem {
    position: absolute;
    left: 52px;
    top: 120px;
    width: 200px;
    height: 210px;
    border-radius: 50%;
  }
  .label--hazelnut .label__emblem {
    background: radial-gradient(circle at 55% 55%, rgba(255,255,255,0.55) 0%, rgba(176,106,44,0.45) 30%, rgba(35,31,32,0) 70%);
  }
  .label--vanilla .label__emblem {
    background: radial-gradient(circle at 55% 55%, rgba(255,255,255,0.6) 0%, rgba(201,202,205,0.4) 30%, rgba(35,31,32,0) 70%);
  }
  .label--caramel .label__emblem {
    background: radial-gradient(circle at 55% 55%, rgba(255,255,255,0.55) 0%, rgba(242,204,71,0.45) 30%, rgba(35,31,32,0) 70%);
  }
  .label__flavour {
    position: absolute;
    top: 338px;
    left: 0;
    width: 100%;
    text-align: center;
    font-size: 54px;
    font-weight: 500;
    line-height: 1;
    -webkit-background-clip: text;
    background-clip: text;
    color: transparent;
  }
  .label--hazelnut .label__flavour {
    background-image: linear-gradient(90deg, var(--copper-dark) 10%, var(--copper-mid) 35%, var(--copper-light) 60%, var(--copper-mid) 90%);
  }
  .label--vanilla .label__flavour {
    background-image: linear-gradient(90deg, var(--silver-light), #ffffff 50%, var(--silver-mid));
  }
  .label--caramel .label__flavour {
    background-image: linear-gradient(90deg, var(--gold-light), var(--gold-mid) 45%, var(--gold-light) 75%, var(--gold-mid));
  }
  .label__band {
    position: absolute;
    left: 2px;
    right: 2px;
    top: 422px;
    height: 44px;
    display: flex;
    align-items: center;
    justify-content: center;
    font-size: 23px;
    font-weight: 500;
    color: var(--band-ink);
  }
  .label--hazelnut .label__band {
    background: linear-gradient(100deg, var(--copper-dark) 0%, var(--copper-mid) 25%, var(--copper-light) 60%, #fbeee0 75%, var(--copper-mid) 100%);
  }
  .label--vanilla .label__band {
    background: linear-gradient(100deg, var(--silver-dark) 0%, var(--silver-light) 35%, var(--silver-mid) 60%, #ffffff 80%, var(--silver-dark) 100%);
  }
  .label--caramel .label__band {
    background: linear-gradient(100deg, var(--gold-mid) 0%, var(--gold-light) 30%, var(--gold-mid) 60%, var(--gold-light) 80%, var(--gold-dark) 100%);
  }
</style>
</head>
<body>
<div class="canvas">
  <section class="label label--hazelnut">
    <div class="label__brand">Brightcup</div>
    <div class="label__emblem" role="img" aria-label="Copper spiral drop emblem with soft glow"></div>
    <div class="label__flavour">Hazlenut</div>
    <div class="label__band">Coffee Syrup</div>
  </section>
  <section class="label label--vanilla">
    <div class="label__brand">Brightcup</div>
    <div class="label__emblem" role="img" aria-label="Silver spiral drop emblem with soft glow"></div>
    <div class="label__flavour">Vanilla</div>
    <div class="label__band">Coffee Syrup</div>
  </section>
  <section class="label label--caramel">
    <div class="label__brand">Brightcup</div>
    <div class="label__emblem" role="img" aria-label="Gold spiral drop emblem with soft glow"></div>
    <div class="label__flavour">Caramel</div>
    <div class="label__band">Coffee Syrup</div>
  </section>
</div>
</body>
</html>
```